BrightLoop - IT services company
Refresh Stationary
Project: BrightLoop - IT services company
BrightLoop  - IT services company -
Creative Brief
Simple
Delia Okonjo
Marketing Manager
2418 Fenwick Lane Suite 140 Durham, NC 27705
delia.okonjo@brightloop-example.com
www.brightloop-example.com

```html
<!DOCTYPE html>
<html lang="en">
<head>
<meta charset="utf-8">
<title>BrightLoop Stationery</title>
<link href="https://fonts.googleapis.com/css2?family=Arimo:wght@400;700&display=swap" rel="stylesheet">
<style>
  :root {
    --navy: #1d3565;
    --blue: #2a5aa8;
    --orange: #e8641e;
    --paper: #ffffff;
    --strip: #ececec;
    --panel: #d6d5d3;
    --disc: #f4f4f3;
    --hub: #dcdbd9;
    --ink: #333333;
    --shadow: rgba(0,0,0,0.18);
  }
  * { box-sizing: border-box; margin: 0; padding: 0; }
  html, body { width: 1200px; height: 871px; overflow: hidden; background: #ffffff; }
  body { position: relative; font-family: "Arimo", Arial, sans-serif; color: var(--ink); }

  .sheet { position: absolute; background: var(--paper); box-shadow: 2px 3px 6px var(--shadow); overflow: hidden; }

  .brand { position: absolute; display: flex; align-items: center; gap: 6px; z-index: 1; }
  .brand-dot { background: var(--orange); flex: none; }
  .brand-name { color: var(--navy); font-weight: 700; letter-spacing: 0.5px; line-height: 1; }
  .tagline { position: absolute; color: var(--blue); font-weight: 700; letter-spacing: 0.3px; white-space: nowrap; z-index: 1; }

  .decor { position: absolute; display: block; }
  .decor .panel { fill: var(--panel); }
  .decor .disc { fill: var(--disc); }
  .decor .hub { fill: var(--hub); }

  /* Letterhead */
  .letterhead { left: 12px; top: 74px; width: 576px; height: 796px; }
  .letterhead .side-strip { position: absolute; left: 0; top: 0; width: 150px; height: 100%; background: var(--strip); }
  .letterhead .decor { left: 150px; top: 0; width: 426px; height: 796px; }
  .letterhead .brand { left: 22px; top: 34px; }
  .letterhead .brand-dot { width: 22px; height: 22px; }
  .letterhead .brand-name { font-size: 30px; }
  .letterhead .tagline { left: 22px; top: 92px; font-size: 15px; }
  .contact { position: absolute; font-size: 10px; font-weight: 700; line-height: 1.55; color: var(--ink); z-index: 1; }
  .contact .label { display: inline-block; width: 42px; }
  .letterhead .contact { left: 10px; top: 330px; }
  .letterhead .address { margin-top: 10px; }
  .web { position: absolute; color: var(--ink); white-space: nowrap; z-index: 1; }
  .letterhead .web { left: 150px; bottom: 18px; width: 426px; text-align: center; font-size: 20px; letter-spacing: 3px; }

  /* Business card */
  .card { left: 608px; top: 74px; width: 238px; height: 128px; }
  .card .decor { left: 0; top: 0; width: 238px; height: 128px; }
  .card .brand { left: 8px; top: 12px; gap: 4px; }
  .card .brand-dot { width: 9px; height: 9px; }
  .card .brand-name { font-size: 12px; }
  .card .tagline { left: 8px; top: 30px; font-size: 6px; }
  .card .person { position: absolute; left: 8px; top: 78px; z-index: 1; }
  .card .person-name { color: var(--orange); font-size: 10px; font-weight: 700; }
  .card .person-role { font-size: 6px; margin-top: 2px; }
  .card .email { position: absolute; right: 8px; top: 12px; font-size: 5.5px; text-align: right; line-height: 1.6; z-index: 1; }
  .card .contact { left: 140px; top: 42px; font-size: 5.5px; font-weight: 400; }
  .card .contact .label { width: 22px; }
  .card .address { margin-top: 6px; }

  /* Envelope */
  .envelope { left: 608px; top: 220px; width: 580px; height: 258px; }
  .envelope .decor { left: 0; top: 0; width: 580px; height: 258px; }
  .envelope .brand { left: 26px; top: 18px; }
  .envelope .brand-dot { width: 18px; height: 18px; }
  .envelope .brand-name { font-size: 25px; }
  .envelope .tagline { left: 26px; top: 66px; font-size: 12px; }
  .envelope .return-address { position: absolute; left: 26px; top: 92px; font-size: 9px; font-weight: 700; z-index: 1; }
  .envelope .web { left: 26px; bottom: 30px; font-size: 14px; letter-spacing: 4px; }
</style>
</head>
<body>

<section class="sheet letterhead">
  <div class="side-strip"></div>
  <svg class="decor" viewBox="0 0 426 796" role="img" aria-label="Large soft grey gear decoration">
    <rect class="panel" x="0" y="0" width="426" height="330"/>
    <circle class="disc" cx="205" cy="560" r="300"/>
    <circle class="hub" cx="215" cy="580" r="100"/>
  </svg>
  <div class="brand"><span class="brand-dot"></span><span class="brand-name">BRIGHTLOOP</span></div>
  <div class="tagline">MANAGED IT SERVICES</div>
  <div class="contact">
    <div><span class="label">Toll free</span>(800) 555 0142</div>
    <div><span class="label">Phone</span>919 555 0186</div>
    <div><span class="label">Fax</span>919 555 0173</div>
    <div class="address">2418 Fenwick Lane,Suite 140<br>Durham, NC 27705</div>
  </div>
  <div class="web">www.brightloop-example.com</div>
</section>

<section class="sheet card">
  <svg class="decor" viewBox="0 0 238 128" role="img" aria-label="Soft grey gear decoration">
    <rect class="panel" x="66" y="0" width="172" height="60"/>
    <circle class="disc" cx="150" cy="85" r="62"/>
  </svg>
  <div class="brand"><span class="brand-dot"></span><span class="brand-name">BRIGHTLOOP</span></div>
  <div class="tagline">MANAGED IT SERVICES</div>
  <div class="email">delia.okonjo@brightloop-example.com<br>www.brightloop-example.com</div>
  <div class="contact">
    <div><span class="label">Toll free</span>(800) 555 0142</div>
    <div><span class="label">Phone</span>919 555 0186</div>
    <div><span class="label">Cell</span>919 555 0121</div>
    <div><span class="label">Fax</span>919 555 0173</div>
    <div class="address">2418 Fenwick Lane,Suite 140<br>Durham, NC 27705</div>
  </div>
  <div class="person">
    <div class="person-name">Delia Okonjo</div>
    <div class="person-role">Marketing Manager</div>
  </div>
</section>

<section class="sheet envelope">
  <svg class="decor" viewBox="0 0 580 258" role="img" aria-label="Soft grey gear decoration">
    <rect class="panel" x="200" y="0" width="380" height="258"/>
    <circle class="disc" cx="348" cy="110" r="120"/>
    <circle class="hub" cx="348" cy="110" r="70"/>
    <circle class="disc" cx="540" cy="250" r="85"/>
  </svg>
  <div class="brand"><span class="brand-dot"></span><span class="brand-name">BRIGHTLOOP</span></div>
  <div class="tagline">MANAGED IT SERVICES</div>
  <div class="return-address">2418 Fenwick Lane,Suite 140, Durham, NC 27705</div>
  <div class="web">www.brightloop-example.com</div>
</section>

</body>
</html>
```